13 Tavo - new website design project

Our company Tavo Electrical is developing a new lead generation website focused on Electrical, LED Lighting and Solar Power. We need a high converting website.

Example of our current website is www.tavoelectrical.com.au You can take content from this website for this new design. Our colours are red, black and white. For our new website we would like to promote Tavo, Bright Days Ahead. Please listen to the jingle.

The below link is the company jingle that we have developed.
http://www.tunecraftaudio.com.au/tav-tc-v1/

The key for this brief is to generate leads for Electrical, LED Lighting (for commercial) and Solar Power & Storage.

Target Market(s)

Business owners in Melbourne Victoria

Number of Pages Required

4 page

Colors
ec1f27
ffffff

Requirements
Must have
• This page must be clean, be in line with company branding and a high converting lead website.

```html
<!DOCTYPE html>
<html lang="en">
<head>
<meta charset="utf-8">
<title>Tavo Electrical – Website Design</title>
<link rel="stylesheet" href="https://fonts.googleapis.com/css2?family=Michroma&family=PT+Sans:ital,wght@0,400;0,700;1,400&display=swap">
<style>
:root{
  --red:#ec1f27;
  --deep-red:#b3141b;
  --ink:#3a3b40;
  --black:#0b0b0b;
  --charcoal:#333335;
  --slate:#5b5b5d;
  --mist:#d9d9d9;
  --paper:#ffffff;
  --line:#c9c9c9;
}
*{box-sizing:border-box;margin:0;padding:0}
html,body{width:720px;height:1200px;overflow:hidden;background:var(--paper)}
body{position:relative;font-family:"PT Sans",sans-serif;color:var(--ink)}
.abs{position:absolute}
.page-rule{position:absolute;top:0;width:1px;height:1200px;background:var(--line)}
.wide{font-family:"Michroma",sans-serif}
.photo{position:absolute}

/* brand lockup */
.brand{position:absolute;text-align:center;color:var(--ink);font-family:"Michroma",sans-serif}
.brand .name{display:block;line-height:1}
.brand .sub{display:block;line-height:1}
.brand .dot{position:absolute;border-radius:50%;background:var(--red)}

/* phone badge */
.phone-badge{position:absolute;background:var(--paper);clip-path:polygon(8% 0,100% 0,100% 100%,0 100%);box-shadow:0 1px 3px rgba(0,0,0,.25);text-align:right;padding-right:4px}
.phone-badge .num{display:flex;align-items:center;justify-content:flex-end;gap:2px;color:var(--red);font-family:"PT Sans",sans-serif;line-height:1}
.phone-badge .num svg{fill:var(--ink)}
.phone-badge .tag{display:block;font-family:"Michroma",sans-serif;color:var(--black);line-height:1}

/* mockups */
.mockup{position:absolute;background:var(--paper);box-shadow:0 2px 6px rgba(0,0,0,.35);overflow:hidden}
.nav{position:absolute;display:flex;font-family:"Michroma",sans-serif;color:var(--paper);font-size:7.5px;letter-spacing:.8px}
.nav span{padding:0 4px;border-left:1px solid rgba(255,255,255,.5);line-height:18px}
.nav span:first-child{border-left:none}
.subnav{position:absolute;display:flex;gap:20px;font-family:"Michroma",sans-serif;color:var(--mist);font-size:7px;letter-spacing:.8px}
.hero{position:absolute;background:var(--black);overflow:hidden}
.circle-photo{position:absolute;border-radius:50%;border:2px solid var(--paper)}
.story-copy{position:absolute;font-size:5px;line-height:1.45;color:#222}
.story-copy p{margin-bottom:4px}
.promise h3{font-size:9.5px;color:var(--deep-red);font-weight:700;margin-bottom:7px}
.promise p{font-size:5px;line-height:1.4;color:#222;margin-bottom:7px}

/* clients */
.clients-band{position:absolute;left:0;top:838px;width:720px;height:53px;background:var(--charcoal)}
.client{position:absolute;top:8px;height:36px;width:65px;display:flex;align-items:center;justify-content:center;font-family:"PT Sans",sans-serif;font-weight:700;font-size:9px;text-align:center;line-height:1}

/* testimonial */
.testimonial{position:absolute;left:422px;top:916px;width:298px;height:94px;background:var(--slate)}
.testimonial .quote{position:absolute;left:134px;top:7px;width:146px;font-size:7px;font-style:italic;color:var(--paper);line-height:1.3}
</style>
</head>
<body>

<div class="page-rule" style="left:66px"></div>
<div class="page-rule" style="left:654px"></div>

<!-- top header band -->
<svg class="abs" style="left:0;top:0" width="720" height="120" viewBox="0 0 720 120">
  <defs>
    <linearGradient id="topShade" x1="0" y1="0" x2="1" y2="0">
      <stop offset="0" stop-color="#6c6c6c"/><stop offset="1" stop-color="#bdbdbd"/>
    </linearGradient>
  </defs>
  <g role="img" aria-label="Black and white photo of an industrial warehouse ceiling">
    <path d="M0 0 H300 L255 62 C170 62 70 45 0 22 Z" fill="url(#topShade)"/>
    <path d="M440 0 H720 V10 C640 45 560 60 470 62 L490 40 L455 40 Z" fill="url(#topShade)"/>
  </g>
  <path d="M0 18 C80 48 170 62 262 64 L258 70 C165 68 75 55 0 30 Z" fill="var(--deep-red)"/>
  <path d="M470 62 C560 60 640 44 720 6 V18 C640 55 560 70 466 70 Z" fill="var(--deep-red)"/>
</svg>

<div class="brand" style="left:246px;top:68px;width:236px">
  <span class="dot" style="left:6px;top:6px;width:26px;height:26px"></span>
  <span class="name" style="font-size:40px;letter-spacing:2px;padding-left:30px">TAVO</span>
  <span class="sub" style="font-size:9px;letter-spacing:9px;margin-top:8px;padding-left:30px">ELECTRICAL</span>
</div>

<div class="phone-badge" style="left:612px;top:100px;width:102px;height:32px">
  <span class="num" style="font-size:21px"><svg width="15" height="12" viewBox="0 0 24 20"><path d="M2 8c0-5 20-5 20 0v2h-6V7H8v3H2zM5 11h14l2 8H3z"/></svg>137261</span>
  <span class="tag" style="font-size:8px;letter-spacing:5px">TAVO</span>
</div>

<!-- mockup 1: home page -->
<div class="mockup" style="left:88px;top:150px;width:552px;height:312px">
  <svg class="abs" style="left:0;top:0" width="552" height="104" viewBox="0 0 552 104">
    <rect width="552" height="104" fill="#2a2a2c"/>
    <rect role="img" aria-label="Dark photo of a commercial building interior" x="90" y="0" width="462" height="60" fill="#4a4a4c"/>
    <path d="M0 0 H100 L80 42 H0 Z" fill="var(--paper)"/>
    <path d="M90 52 C240 70 420 60 552 30 V38 C420 70 240 80 90 60 Z" fill="var(--deep-red)"/>
    <path d="M35 50 H66 L50 104 H22 Z" fill="var(--paper)"/>
  </svg>
  <div class="brand" style="left:10px;top:14px;width:80px;text-align:left">
    <span class="name" style="font-size:13px;letter-spacing:1px">TAVO</span>
    <span class="sub" style="font-size:3px;letter-spacing:3px;margin-top:2px">ELECTRICAL</span>
  </div>
  <div class="nav" style="left:210px;top:14px"><span>HOME</span><span>TAVO STORY</span><span>OUR WORK</span><span>CONTACT US</span></div>
  <div class="subnav" style="left:117px;top:76px"><span>ELECTRICAL</span><span>LED LIGHTING</span><span>SOLAR POWER</span></div>
  <div class="phone-badge" style="left:472px;top:53px;width:80px;height:26px">
    <span class="num" style="font-size:17px"><svg width="12" height="10" viewBox="0 0 24 20"><path d="M2 8c0-5 20-5 20 0v2h-6V7H8v3H2zM5 11h14l2 8H3z"/></svg>137261</span>
    <span class="tag" style="font-size:6px;letter-spacing:4px">TAVO</span>
  </div>
  <div class="hero" style="left:0;top:102px;width:552px;height:168px">
    <div class="circle-photo" role="img" aria-label="Photo of an LED-lit warehouse interior" style="left:398px;top:-24px;width:116px;height:116px;background:radial-gradient(circle at 50% 30%,#d8dde4,#5d6470)"></div>
    <div class="circle-photo" role="img" aria-label="Photo of rooftop solar panels" style="left:330px;top:58px;width:116px;height:116px;background:linear-gradient(135deg,#a9bad6,#2e4a82)"></div>
    <div class="circle-photo" role="img" aria-label="Photo of an electrician working on a switchboard" style="left:456px;top:76px;width:100px;height:100px;background:radial-gradient(circle,#d7b98f,#6c5a48)"></div>
    <div class="abs wide" style="left:4px;top:96px;color:var(--paper);font-size:17px">TAVO</div>
    <div class="abs" style="left:101px;top:101px;color:var(--red);font-size:10.5px;letter-spacing:.2px">ELECTRICALS. LED LIGHTING. SOLAR POWER.</div>
    <div class="abs" style="left:2px;top:116px;color:var(--paper);font-size:9.5px">Australia's largest fully integrated Electrical &amp; Energy Solutions provider.</div>
  </div>
  <div class="abs" style="left:14px;top:274px;width:518px;height:38px;background:var(--charcoal)"></div>
</div>
<div class="abs" style="left:128px;top:462px;width:466px;height:10px;background:var(--charcoal)"></div>

<!-- mockup 2: story page -->
<div class="mockup" style="left:92px;top:472px;width:546px;height:310px">
  <div class="abs" style="left:0;top:0;width:546px;height:72px;background:var(--black);overflow:hidden">
    <div class="circle-photo" role="img" aria-label="Photo of solar panels" style="left:320px;top:-24px;width:96px;height:96px;background:linear-gradient(135deg,#a9bad6,#2e4a82)"></div>
    <div class="circle-photo" role="img" aria-label="Photo of a hand holding a multimeter" style="left:406px;top:-14px;width:76px;height:76px;background:radial-gradient(circle,#d9b892,#8a6b58)"></div>
    <div class="circle-photo" role="img" aria-label="Photo of ceiling lighting" style="left:480px;top:-10px;width:72px;height:72px;background:radial-gradient(circle,#e4e4e4,#777)"></div>
    <div class="abs wide" style="left:28px;top:34px;color:var(--paper);font-size:20px">TAVO</div>
  </div>
  <div class="abs" style="left:0;top:72px;width:546px;height:3px;background:var(--deep-red)"></div>
  <div class="abs wide" style="left:120px;top:72px;width:80px;height:20px;background:var(--paper);box-shadow:0 1px 3px rgba(0,0,0,.3);font-size:6.5px;letter-spacing:1px;text-align:center;line-height:20px">TAVO STORY</div>
  <div class="phone-badge" style="left:466px;top:62px;width:80px;height:26px">
    <span class="num" style="font-size:17px"><svg width="12" height="10" viewBox="0 0 24 20"><path d="M2 8c0-5 20-5 20 0v2h-6V7H8v3H2zM5 11h14l2 8H3z"/></svg>137261</span>
    <span class="tag" style="font-size:6px;letter-spacing:4px">TAVO</span>
  </div>

  <div class="photo" role="img" aria-label="Photo of the company warehouse floor" style="left:66px;top:104px;width:106px;height:72px;background:linear-gradient(180deg,#8c8e86,#4e5a48 60%,#6b6f62)"></div>
  <div class="abs" style="left:66px;top:182px;color:var(--deep-red);font-size:14px;font-weight:700">The Tavo Story</div>
  <div class="abs" style="left:66px;top:200px;color:var(--deep-red);font-size:8.5px;font-weight:700">Tavo Electrical. REC #20417.</div>

  <div class="story-copy" style="left:180px;top:104px;width:172px">
    <p>Message From The Director</p>
    <p>Electrical and Energy Solutions are at the forefront of our company. Tavo Electrical has a long history in Electrical, LED Lighting and Solar Power and just like the Cougar, we will strive to be fierce &amp; agile in an effort to exceed our customer's expectations and develop stronger links with all our business partners &amp; community.</p>
    <p>Tavo Electrical is an expert Electrical Company providing services to all Residential and Commercial customers. With over 10 years of experience, Tavo Electrical has developed a highly-experienced team of professionals that ensure all our customer expectations are exceeded. Our team comprise of over 70 staff of Designers, Consultants, Electricians who provide expert advice and quality of installation at an affordable price.</p>
  </div>
  <div class="photo" role="img" aria-label="Handwritten director's signature" style="left:360px;top:140px;width:60px;height:20px;background:linear-gradient(90deg,#f1f1f1,#e2e2e2)"></div>
  <div class="abs" style="left:362px;top:197px;font-size:6px;font-style:italic;color:var(--deep-red)">Read more</div>

  <div class="abs promise" style="left:180px;top:222px;width:304px">
    <h3>Our promise – Quality, Reliability and Customers First</h3>
    <p>Quality Our focus is on quality while maintaining great value for money. We are committed to leading the market with the products that we offer our valuable customers</p>
    <p>Reliability You can count on us to get the job done. We are well organised, professional and turn up when we say we will.</p>
    <p>Customer First Customers are the key focus of our business. Our highly-experienced team of Consultants and Electricians are dedicated to ensure all customer needs are met.</p>
  </div>
</div>
<div class="abs" style="left:128px;top:782px;width:466px;height:28px;background:var(--charcoal)"></div>

<div class="abs" style="left:0;top:815px;width:756px;text-align:center;font-size:11px;font-style:italic;color:#222">Our satisfied clients include...</div>

<div class="clients-band">
  <div class="client" style="left:215px;background:var(--paper);color:var(--red);font-weight:400;font-size:11px">Velvetia</div>
  <div class="client" style="left:296px;width:64px;background:#fff200;color:#222">Outback Surplus</div>
  <div class="client" style="left:374px;width:64px;background:#d52b1e;color:var(--paper)">Heron Plumbing</div>
  <div class="client" style="left:451px;width:64px;background:#c1121b;color:#ffcc00">Goldarch Burgers</div>
</div>

<div class="phone-badge" style="left:320px;top:916px;width:100px;height:32px">
  <span class="num" style="font-size:21px"><svg width="15" height="12" viewBox="0 0 24 20"><path d="M2 8c0-5 20-5 20 0v2h-6V7H8v3H2zM5 11h14l2 8H3z"/></svg>137261</span>
  <span class="tag" style="font-size:8px;letter-spacing:5px">TAVO</span>
</div>

<div class="testimonial">
  <div class="abs" style="left:13px;top:12px;width:114px;height:22px;background:var(--paper);display:flex;align-items:center;gap:4px;padding-left:4px">
    <span style="width:8px;height:8px;background:#777"></span>
    <span style="font-size:9px;font-weight:700;color:var(--deep-red)">CARROW SIGNS</span>
  </div>
  <div class="photo" role="img" aria-label="Photo of a sign workshop interior" style="left:13px;top:34px;width:114px;height:50px;background:linear-gradient(180deg,#b5aca0,#6b6560)"></div>
  <div class="quote">I found Marcus to be well organised, punctual, professional and a good communicator. He did the job at a very reasonable price. A pleasure to deal with."<br><br>Rico T.<br>Mount Waverley VIC</div>
  <svg class="abs" style="left:284px;top:6px" width="9" height="9" viewBox="0 0 9 9"><path d="M1 1L8 8M8 1L1 8" stroke="#ccc" stroke-width="1.2"/></svg>
</div>

<!-- footer brand band -->
<svg class="abs" style="left:0;top:1008px" width="720" height="192" viewBox="0 0 720 192">
  <defs>
    <linearGradient id="redShade" x1="0" y1="0" x2="0" y2="1">
      <stop offset="0" stop-color="#8e2a2a"/><stop offset="1" stop-color="#c8383a"/>
    </linearGradient>
  </defs>
  <g role="img" aria-label="Red-tinted photo of a commercial building">
    <path d="M0 40 C40 30 90 22 150 18 L120 100 H0 Z" fill="url(#redShade)"/>
    <path d="M0 100 H120 L100 192 H0 Z" fill="url(#redShade)"/>
    <path d="M560 18 C630 22 680 34 720 48 V192 H600 L620 130 H575 Z" fill="url(#redShade)"/>
  </g>
</svg>
<div class="brand" style="left:150px;top:1040px;width:420px">
  <span class="dot" style="left:0;top:10px;width:58px;height:58px"></span>
  <span class="name" style="font-size:78px;letter-spacing:2px;padding-left:56px">TAVO</span>
  <span class="sub" style="font-size:17px;letter-spacing:20px;margin-top:14px;padding-left:40px">ELECTRICAL</span>
</div>

</body>
</html>
```